"Fight Back" banner ad design

We have sketched the design and have images to consider including. We are looking for something striking, FIGHT BACK! with a clenched fist image, then a fading images of variance.png and hi-bill.png in the background. Tag line "Fight your water bill with your own data" optionally include "Crest View" rivo3159 logo, KMPT Design, LLC based in San Diego CA. Pre-order now, visit https://www.raisenest.com/rivoplume @rivo3159, info@rivo3159.com

"Fight your water bill with your own data"

```html
<!DOCTYPE html>
<html lang="en">
<head>
<meta charset="utf-8">
<title>Fight Back! – rivo3159</title>
<link rel="stylesheet" href="https://fonts.googleapis.com/css2?family=Montserrat:wght@600&family=Comfortaa:wght@700&family=Arimo:wght@700&display=swap">
<style>
  :root {
    --teal-title: #3a7a8c;
    --teal-dark: #215d72;
    --teal-light: #86c9dc;
    --tag-blue: #1e4f9e;
    --ink: #111111;
    --paper: #ffffff;
    --skin-light: #f1d3bd;
    --skin-mid: #e2b394;
    --bill-fade: #e9eef1;
  }
  html, body {
    margin: 0;
    padding: 0;
    overflow: hidden;
    background: var(--paper);
  }
  .banner {
    position: relative;
    width: 1200px;
    height: 662px;
    overflow: hidden;
    background: var(--paper);
  }
  .statement-backdrop {
    position: absolute;
    left: 268px;
    top: 16px;
    width: 458px;
    height: 646px;
    background: linear-gradient(180deg, var(--bill-fade) 0%, #f6f8f9 60%, var(--paper) 100%);
    opacity: 0.8;
  }
  .fist-photo {
    position: absolute;
    left: 0;
    top: 0;
    width: 730px;
    height: 500px;
    background:
      radial-gradient(ellipse 260px 240px at 360px 250px, var(--skin-mid) 0%, var(--skin-light) 55%, rgba(241, 211, 189, 0) 100%),
      linear-gradient(180deg, rgba(233, 238, 241, 0) 0%, rgba(233, 238, 241, 0.6) 30%, rgba(233, 238, 241, 0.6) 60%, rgba(255, 255, 255, 0) 100%);
  }
  .headline {
    position: absolute;
    left: 498px;
    top: 12px;
    margin: 0;
    font-family: "Montserrat", sans-serif;
    font-weight: 600;
    font-size: 108px;
    line-height: 1;
    letter-spacing: -3px;
    color: var(--teal-title);
    white-space: nowrap;
    text-shadow: 0 0 6px var(--paper), 0 0 3px var(--paper);
  }
  .tagline {
    position: absolute;
    left: 744px;
    top: 146px;
    margin: 0;
    font-family: "Comfortaa", sans-serif;
    font-weight: 700;
    font-size: 42px;
    line-height: 54px;
    letter-spacing: -0.5px;
    color: var(--tag-blue);
    text-shadow: 2px 3px 4px rgba(0, 0, 0, 0.35);
    white-space: nowrap;
  }
  .usage-chart {
    position: absolute;
    left: 588px;
    top: 280px;
    width: 606px;
    height: 368px;
    background: var(--paper);
  }
  .chart-title { font-family: "Arimo", sans-serif; font-weight: 700; font-size: 21px; fill: var(--paper); }
  .chart-legend { font-family: "Arimo", sans-serif; font-weight: 700; font-size: 15px; fill: var(--ink); }
  .chart-axis { font-family: "Arimo", sans-serif; font-weight: 700; font-size: 13px; fill: var(--ink); }
  .bar-previous { fill: var(--teal-light); stroke: var(--ink); stroke-width: 1; }
  .bar-current { fill: var(--teal-dark); stroke: var(--ink); stroke-width: 1; }
  .contact {
    position: absolute;
    left: 12px;
    top: 512px;
    margin: 0;
    font-family: "Comfortaa", sans-serif;
    font-weight: 700;
    font-size: 25px;
    line-height: 34px;
    letter-spacing: 0.3px;
    color: var(--ink);
    white-space: nowrap;
  }
</style>
</head>
<body>
<main class="banner">
  <div class="statement-backdrop" role="img" aria-label="Faded water bill statement showing fees and charges"></div>

  <div class="fist-photo" role="img" aria-label="Photo of a clenched fist squeezing a rolled water bill"></div>

  <h1 class="headline">FIGHT BACK!</h1>

  <p class="tagline">Fight your water bill<br>with your own data.</p>

  <svg class="usage-chart" viewBox="0 0 606 368" aria-label="Water use in HCF, previous year versus current year">
    <rect x="0.5" y="0.5" width="605" height="367" fill="none" stroke="var(--teal-dark)" stroke-width="1"/>
    <rect x="0" y="0" width="606" height="30" fill="var(--teal-dark)"/>
    <text class="chart-title" x="303" y="23" text-anchor="middle">WATER USE IN HCF (Hundred Cubic Feet)</text>

    <rect x="157" y="36" width="16" height="16" fill="var(--teal-light)" stroke="var(--ink)"/>
    <text class="chart-legend" x="190" y="50">Previous Year</text>
    <rect x="318" y="36" width="16" height="16" fill="var(--teal-dark)" stroke="var(--ink)"/>
    <text class="chart-legend" x="351" y="50">Current Year</text>

    <g stroke="var(--ink)" stroke-width="1.5">
      <line x1="36" y1="59" x2="597" y2="59"/><line x1="36" y1="78" x2="597" y2="78"/>
      <line x1="36" y1="97" x2="597" y2="97"/><line x1="36" y1="116" x2="597" y2="116"/>
      <line x1="36" y1="136" x2="597" y2="136"/><line x1="36" y1="155" x2="597" y2="155"/>
      <line x1="36" y1="174" x2="597" y2="174"/><line x1="36" y1="193" x2="597" y2="193"/>
      <line x1="36" y1="212" x2="597" y2="212"/><line x1="36" y1="232" x2="597" y2="232"/>
      <line x1="36" y1="251" x2="597" y2="251"/><line x1="36" y1="270" x2="597" y2="270"/>
      <line x1="36" y1="289" x2="597" y2="289"/><line x1="36" y1="308" x2="597" y2="308"/>
      <line x1="36" y1="328" x2="597" y2="328"/><line x1="36" y1="347" x2="597" y2="347"/>
      <line x1="36" y1="366" x2="597" y2="366"/>
    </g>
    <g class="chart-axis" text-anchor="end">
      <text x="30" y="64">80</text><text x="30" y="83">75</text><text x="30" y="102">70</text>
      <text x="30" y="121">65</text><text x="30" y="141">60</text><text x="30" y="160">55</text>
      <text x="30" y="179">50</text><text x="30" y="198">45</text><text x="30" y="217">40</text>
      <text x="30" y="237">35</text><text x="30" y="256">30</text><text x="30" y="275">25</text>
      <text x="30" y="294">20</text><text x="30" y="313">15</text><text x="30" y="333">10</text>
      <text x="30" y="352">5</text><text x="30" y="370">0</text>
    </g>

    <rect class="bar-previous" x="82" y="262" width="19" height="104"/>
    <rect class="bar-current" x="106" y="278" width="19" height="88"/>
    <rect class="bar-previous" x="176" y="235" width="19" height="131"/>
    <rect class="bar-current" x="200" y="289" width="19" height="77"/>
    <rect class="bar-previous" x="270" y="295" width="19" height="71"/>
    <rect class="bar-current" x="294" y="289" width="19" height="77"/>
    <rect class="bar-previous" x="365" y="253" width="19" height="113"/>
    <rect class="bar-current" x="388" y="63" width="19" height="303"/>
    <rect class="bar-previous" x="459" y="270" width="19" height="96"/>
    <rect class="bar-current" x="483" y="105" width="19" height="261"/>
    <rect class="bar-previous" x="554" y="270" width="19" height="96"/>
    <rect class="bar-current" x="578" y="86" width="19" height="280"/>
  </svg>

  <p class="contact">LLC based in San Diego CA.<br>Pre-order now,<br>visit https://www.raisenest.com<br>rivoplume @rivo3159, info@rivo3159.com</p>
</main>
</body>
</html>
```